Food truck menu design

Looking for a menu to be dissed for my toasted sandwich food truck. I have attached to logo and photo of the food truck for inspiration. if it can tie into them.
needing three sections, with titles:
CLASSICS
- classic one
. description
-Classic two
. Description
PREMIUM
- Premium one
. description
-Premium Two
. Description
-Premium Three
. Description
DESERT
-Desert one
. Description
-Desert two
.Description

also if it can be editable so I can change menu items and descriptions.

```html
<!DOCTYPE html>
<html lang="en">
<head>
<meta charset="utf-8">
<title>Toasted Sandwich Menu</title>
<link rel="stylesheet" href="https://fonts.googleapis.com/css2?family=Lobster&family=Oswald:wght@700&family=Libre+Baskerville&family=Alegreya:wght@400;700&family=Arvo:wght@700&display=swap">
<style>
  :root {
    --stage: #3b4048;
    --menu-black: #070606;
    --menu-brown: #2a1a0e;
    --orange: #f4a323;
    --white: #ffffff;
    --muted: #d9d4cc;
    --rule: #cfcfcf;
  }
  * { margin: 0; padding: 0; box-sizing: border-box; }
  html, body { width: 1072px; height: 1200px; overflow: hidden; }
  body { background: var(--stage); position: relative; font-family: "Alegreya", serif; }

  .page {
    position: absolute; top: 244px; width: 821px; height: 1170px;
    background: var(--menu-black); overflow: hidden;
    transform: scale(0.609); transform-origin: top left;
  }
  .page-front { left: 24px; }
  .page-back { left: 548px; }

  .page-backdrop {
    position: absolute; inset: 0;
    background:
      radial-gradient(ellipse 55% 35% at 45% 62%, rgba(90,70,35,.55), transparent 70%),
      radial-gradient(ellipse 40% 20% at 70% 38%, rgba(120,80,30,.35), transparent 70%),
      linear-gradient(180deg, var(--menu-black) 0%, var(--menu-brown) 55%, var(--menu-black) 100%);
  }
  .page-frame { position: absolute; left: 17px; top: 21px; width: 787px; height: 1128px; border: 1.5px solid var(--rule); }

  .title-script { position: absolute; font-family: "Lobster", cursive; color: var(--white); line-height: 1; }
  .title-main { position: absolute; font-family: "Oswald", sans-serif; font-weight: 700; color: var(--orange); line-height: 1; letter-spacing: -1px; }
  .title-menu {
    position: absolute; text-align: center;
    font-family: "Libre Baskerville", serif; color: var(--white); line-height: 1.1;
    border-top: 1.5px solid var(--rule); border-bottom: 1.5px solid var(--rule); padding-top: 2px;
  }

  .front-title .title-script { left: 95px; top: 50px; font-size: 84px; }
  .front-title .title-main { left: 43px; top: 125px; font-size: 104px; transform: scaleX(.92); transform-origin: left; }
  .front-title .title-menu { left: 88px; top: 232px; width: 272px; font-size: 56px; }

  .brand { position: absolute; display: flex; align-items: center; }
  .brand-dot { border-radius: 50%; background: var(--orange); flex: none; }
  .brand-name { font-family: "Alegreya", serif; font-weight: 700; color: var(--orange); white-space: nowrap; }
  .brand-small { left: 482px; top: 140px; gap: 12px; }
  .brand-small .brand-dot { width: 34px; height: 34px; }
  .brand-small .brand-name { font-size: 38px; }

  .photo { position: absolute; border-radius: 50%; box-shadow: 0 0 0 3px #111, 0 0 0 5px var(--white); }
  .photo-ring { position: absolute; border-radius: 50%; border: 1.5px solid var(--white); }
  .photo-sandwich-a { background: radial-gradient(circle at 45% 45%, #e6c89a, #b58550 55%, #6d8e3c 85%); }
  .photo-sandwich-b { background: radial-gradient(circle at 55% 50%, #e0b878, #a6683a 55%, #7a3f22 85%); }
  .photo-sandwich-c { background: radial-gradient(circle at 50% 55%, #f0d6a4, #c9904a 55%, #4a3a2a 90%); }

  .badge {
    position: absolute; border-radius: 50%; background: var(--orange); box-shadow: 0 0 0 2px var(--menu-black);
    display: flex; align-items: center; justify-content: center;
    font-family: "Alegreya", serif; font-weight: 700; color: var(--menu-black);
  }

  .section-banner { position: absolute; width: 245px; height: 43px; }
  .section-banner svg { position: absolute; inset: 0; }
  .section-banner span {
    position: absolute; inset: 0; display: flex; align-items: center; justify-content: center;
    font-family: "Arvo", serif; font-weight: 700; font-size: 24px; color: var(--menu-black); letter-spacing: .5px;
  }

  .item { position: absolute; width: 376px; }
  .item-head { display: flex; justify-content: space-between; align-items: baseline; }
  .item-name { font-family: "Alegreya", serif; font-weight: 700; font-size: 21px; color: var(--white); }
  .item-price { font-family: "Alegreya", serif; font-weight: 700; font-size: 18px; color: var(--white); }
  .item-desc { font-family: "Alegreya", serif; font-size: 14px; line-height: 1.3; color: var(--muted); width: 290px; margin-top: 1px; }

  .back-title .title-script { left: 160px; top: 70px; font-size: 110px; }
  .back-title .title-main { left: 120px; top: 168px; font-size: 134px; transform: scaleX(.92); transform-origin: left; }
  .back-title .title-menu { left: 190px; top: 310px; width: 360px; font-size: 72px; }

  .brand-large { left: 0; right: 0; top: 560px; justify-content: center; gap: 24px; }
  .brand-large .brand-dot { width: 70px; height: 70px; }
  .brand-large .brand-name { font-size: 80px; }

  .cover-photo {
    position: absolute; left: 40px; right: 40px; top: 860px; height: 270px; border-radius: 30px;
    background: radial-gradient(ellipse 30% 45% at 25% 55%, #e2b46a, transparent 75%),
                radial-gradient(ellipse 30% 45% at 75% 55%, #e2b46a, transparent 75%),
                radial-gradient(ellipse 50% 40% at 50% 70%, #b8563a, transparent 80%);
  }
</style>
</head>
<body>
  <main class="page page-front">
    <div class="page-backdrop" role="img" aria-label="Dark blurred photo of a stacked toasted sandwich behind the menu"></div>
    <div class="page-frame"></div>

    <div class="front-title">
      <div class="title-script">Toasted</div>
      <div class="title-main">SANDWICH</div>
      <div class="title-menu">MENU</div>
    </div>

    <div class="brand brand-small">
      <div class="brand-dot"></div>
      <div class="brand-name">Milo's Melts</div>
    </div>

    <div class="photo-ring" style="left:103px;top:335px;width:220px;height:220px;"></div>
    <div class="photo photo-sandwich-a" style="left:112px;top:344px;width:202px;height:202px;" role="img" aria-label="Photo of grilled club sandwich halves with ham and lettuce"></div>
    <div class="badge" style="left:275px;top:481px;width:52px;height:52px;font-size:21px;">$10</div>

    <div class="section-banner" style="left:477px;top:357px;">
      <svg viewBox="0 0 245 43" width="245" height="43"><polygon points="0,0 245,0 226,21.5 245,43 0,43 19,21.5" fill="var(--orange)"/></svg>
      <span>CLASSICS</span>
    </div>
    <div class="item" style="left:410px;top:430px;">
      <div class="item-head"><span class="item-name">Classic One</span><span class="item-price">$ 08</span></div>
      <p class="item-desc">Lorem ipsum dolor sit amet, consectetuer adipiscing elit, sed diam</p>
    </div>
    <div class="item" style="left:410px;top:513px;">
      <div class="item-head"><span class="item-name">Classic Two</span><span class="item-price">$ 10</span></div>
      <p class="item-desc">Lorem ipsum dolor sit amet, consectetuer adipiscing elit, sed diam</p>
    </div>

    <div class="section-banner" style="left:116px;top:598px;">
      <svg viewBox="0 0 245 43" width="245" height="43"><polygon points="0,0 245,0 226,21.5 245,43 0,43 19,21.5" fill="var(--orange)"/></svg>
      <span>PREMIUM</span>
    </div>
    <div class="item" style="left:50px;top:663px;">
      <div class="item-head"><span class="item-name">Premium One</span><span class="item-price">$ 12</span></div>
      <p class="item-desc">Lorem ipsum dolor sit amet, consectetuer adipiscing elit, sed diam</p>
    </div>
    <div class="item" style="left:50px;top:746px;">
      <div class="item-head"><span class="item-name">Premium Two</span><span class="item-price">$ 15</span></div>
      <p class="item-desc">Lorem ipsum dolor sit amet, consectetuer adipiscing elit, sed diam</p>
    </div>
    <div class="item" style="left:50px;top:833px;">
      <div class="item-head"><span class="item-name">Premium Three</span><span class="item-price">$ 17</span></div>
      <p class="item-desc">Lorem ipsum dolor sit amet, consectetuer adipiscing elit, sed diam</p>
    </div>

    <div class="photo-ring" style="left:469px;top:604px;width:260px;height:260px;"></div>
    <div class="photo photo-sandwich-b" style="left:477px;top:612px;width:244px;height:244px;" role="img" aria-label="Photo of club sandwiches with tomatoes, fries and ketchup on a board"></div>
    <div class="badge" style="left:672px;top:775px;width:66px;height:66px;font-size:26px;">$15</div>

    <div class="photo-ring" style="left:117px;top:916px;width:202px;height:202px;"></div>
    <div class="photo photo-sandwich-c" style="left:126px;top:925px;width:184px;height:184px;" role="img" aria-label="Photo of toasted sandwich triangles on a plate"></div>
    <div class="badge" style="left:274px;top:1054px;width:52px;height:52px;font-size:21px;">$13</div>

    <div class="section-banner" style="left:477px;top:912px;">
      <svg viewBox="0 0 245 43" width="245" height="43"><polygon points="0,0 245,0 226,21.5 245,43 0,43 19,21.5" fill="var(--orange)"/></svg>
      <span>DESERT</span>
    </div>
    <div class="item" style="left:413px;top:976px;width:372px;">
      <div class="item-head"><span class="item-name">Desert One</span><span class="item-price">$ 13</span></div>
      <p class="item-desc">Lorem ipsum adipiscing elit, sed diam</p>
    </div>
    <div class="item" style="left:413px;top:1052px;width:372px;">
      <div class="item-head"><span class="item-name">Desert Two</span><span class="item-price">$ 16</span></div>
      <p class="item-desc">Lorem ipsum dolor sit amet, consectetuer adipiscing elit, sed diam</p>
    </div>
  </main>

  <section class="page page-back">
    <div class="page-backdrop" role="img" aria-label="Dark blurred photo of a stacked toasted sandwich behind the cover"></div>
    <div class="page-frame"></div>

    <div class="back-title">
      <div class="title-script">Toasted</div>
      <div class="title-main">SANDWICH</div>
      <div class="title-menu">MENU</div>
    </div>

    <div class="brand brand-large">
      <div class="brand-dot"></div>
      <div class="brand-name">Milo's Melts</div>
    </div>

    <div class="cover-photo" role="img" aria-label="Photo of four grilled sandwich halves with ham, tomato and lettuce"></div>
  </section>
</body>
</html>
```